Velmora Brightstead Website

Create website for Legal Management Company which specializes in Law Office Spersriinal Management
System implementation & Training
Global presence
Paralegal Services - Remote or In-Office
Legal Research
- Judge Motion Ruling History
- Opposing Counsel Opposition Research - Historical Filings - Pattern identification
Service by Mail - Ex- Parte Notice

Probate -Heir Finder - Asset Location -

```html
<!DOCTYPE html>
<html lang="en">
<head>
<meta charset="utf-8">
<title>Velmora Brightstead — Legal Management</title>
<link rel="stylesheet" href="https://fonts.googleapis.com/css2?family=Cormorant+Garamond:ital,wght@0,400;0,500;1,400&family=Plus+Jakarta+Sans:wght@300;400;500;600;700;800&display=swap">
<style>
:root{
  --paper:#fcfbf8;
  --ink:#141414;
  --ink-soft:#4a4f58;
  --navy:#2a3447;
  --gold:#8c6f4e;
  --gold-fill:#8f7352;
  --dark:#121212;
  --dark-line:#2c2c2c;
  --muted:#8f96a3;
  --line:#e6e3dc;
  --bar:#e5e2da;
  --sans:'Plus Jakarta Sans',Arial,sans-serif;
  --serif:'Cormorant Garamond',Georgia,serif;
}
*{box-sizing:border-box;margin:0;padding:0}
html,body{width:1200px;height:2868px;overflow:hidden}
body{background:var(--paper);color:var(--ink);font-family:var(--sans);position:relative}
.eyebrow{font-size:8.5px;letter-spacing:.32em;font-weight:700;color:var(--gold);text-transform:uppercase}

/* header */
.site-header{height:52px;display:flex;align-items:center;justify-content:space-between;padding:0 27px 0 53px;border-bottom:1px solid #efede8}
.brand{font-size:9.5px;font-weight:700;letter-spacing:.34em;padding-bottom:3px;border-bottom:1.5px solid var(--ink)}
.main-nav{display:flex;gap:31px}
.main-nav a{font-size:8.5px;font-weight:700;letter-spacing:.14em;color:var(--ink);text-decoration:none}
.main-nav a.connect{color:var(--gold)}

/* hero */
.hero{height:658px;position:relative}
.hero-title{position:absolute;left:53px;top:182px;font-size:86px;line-height:.9;font-weight:800;letter-spacing:-.045em}
.hero-title em{display:block;font-family:var(--serif);font-weight:400;font-style:italic;color:var(--navy);font-size:80px;letter-spacing:-.01em;line-height:1.05}
.hero-lead{position:absolute;left:53px;top:548px;width:420px;font-size:13.5px;line-height:1.62;color:var(--ink-soft);font-weight:400}
.hero-photo{position:absolute;left:817px;top:115px;width:356px;height:447px;background:linear-gradient(180deg,#6f7377 0%,#262a36 30%,#1b2233 60%,#3d4147 100%)}
.hero-badge{position:absolute;left:18px;right:18px;bottom:20px;background:rgba(244,243,240,.95);padding:18px 18px 17px}
.hero-badge .eyebrow{letter-spacing:.12em;font-size:8px}
.hero-badge p{margin-top:7px;font-size:9.5px;font-weight:500}

/* pillars */
.pillars{background:var(--dark);height:646px;padding:117px 27px 0 53px;position:relative}
.pillars .eyebrow{color:var(--gold)}
.section-title{font-family:var(--serif);font-weight:400;font-size:47px;color:#fff;margin-top:6px}
.pillar-count{position:absolute;right:27px;top:171px;font-size:11px;color:#8a8a8a;letter-spacing:.08em}
.pillar-grid{margin-top:60px;display:grid;grid-template-columns:repeat(4,1fr);border:1px solid var(--dark-line);height:292px}
.pillar{padding:36px 36px;border-right:1px solid var(--dark-line)}
.pillar:last-child{border-right:0}
.pillar svg{width:24px;height:24px;stroke:var(--gold);fill:none;stroke-width:1.5;stroke-linecap:round;stroke-linejoin:round}
.pillar h3{margin-top:36px;color:#fff;font-size:15px;font-weight:700;line-height:1.38;letter-spacing:-.01em;text-transform:uppercase}
.pillar p{margin-top:14px;font-size:10.5px;line-height:1.65;color:#a6a6a6;font-weight:300}

/* analytics */
.analytics{height:567px;position:relative;border-bottom:1px solid #efede8}
.analytics .eyebrow{position:absolute;left:53px;top:66px}
.analytics-title{position:absolute;left:53px;top:82px;font-family:var(--serif);font-weight:400;font-size:58px;line-height:.93}
.analytics-title em{display:block;color:var(--navy)}
.analytics-lead{position:absolute;left:53px;top:216px;width:500px;font-size:13.5px;line-height:1.62;color:var(--ink-soft)}
.insight-list{position:absolute;left:53px;top:296px;width:523px;list-style:none}
.insight{display:flex;gap:18px;padding:6px 0 24px;border-bottom:1px solid var(--line);margin-bottom:24px}
.insight .num{font-family:var(--serif);font-style:italic;font-size:15px;color:var(--gold);width:18px;padding-top:2px}
.insight h4{font-size:13.5px;font-weight:700;letter-spacing:-.01em}
.insight p{margin-top:7px;font-size:9.5px;line-height:1.55;color:var(--muted)}
.report-shadow{position:absolute;left:674px;top:104px;width:524px;height:372px;border:1px solid #dedbd3}
.report{position:absolute;left:648px;top:76px;width:526px;height:372px;background:#fff;box-shadow:0 20px 60px rgba(0,0,0,.08);padding:30px 26px 0 36px;transform:rotate(.6deg)}
.report-head{display:flex;justify-content:space-between;align-items:flex-end;padding-bottom:8px;border-bottom:1.5px solid var(--ink);font-size:7.5px;font-weight:700;letter-spacing:-.02em}
.report-head .tag{color:var(--gold);font-size:7px}
.placeholder{height:14px;background:var(--bar);margin-top:24px;width:347px}
.placeholder.short{width:232px;margin-top:12px}
.metric{margin-top:50px}
.metric + .metric{margin-top:32px}
.metric-row{display:flex;justify-content:space-between;align-items:flex-end}
.metric-row span{font-size:7.5px;font-weight:700;color:var(--muted);letter-spacing:-.01em}
.metric-row b{font-family:var(--serif);font-style:italic;font-weight:400;font-size:17px}
.track{margin-top:8px;height:3px;background:var(--bar)}
.track i{display:block;height:3px}
.report-btn{display:block;margin:36px auto 0;width:152px;background:var(--ink);color:#fff;font-size:8px;font-weight:700;letter-spacing:.06em;text-align:center;padding:10px 0}

/* network */
.network{height:390px;position:relative}
.network-title{position:absolute;left:53px;top:97px;font-family:var(--serif);font-weight:400;font-size:27px;line-height:1.12}
.network-lead{position:absolute;left:53px;top:188px;width:350px;font-size:10.5px;line-height:1.65;color:var(--ink-soft)}
.network-facts{position:absolute;left:53px;top:255px;list-style:none}
.network-facts li{display:flex;align-items:center;gap:12px;font-size:8.5px;font-weight:700;letter-spacing:.08em;margin-bottom:11px}
.network-facts svg{width:12px;height:12px;stroke:var(--gold);fill:none;stroke-width:1.5}
.hub-grid{position:absolute;left:475px;top:97px;width:698px;display:grid;grid-template-columns:repeat(3,217px);gap:24px 24px;grid-auto-rows:103px;justify-content:space-between}
.hub{border:1px solid #e2dfd8;padding:32px 30px;background:var(--paper)}
.hub h5{font-family:var(--serif);font-weight:400;font-size:19px}
.hub span{display:block;margin-top:6px;font-size:7px;font-weight:700;color:var(--muted)}
.hub.pending{border:1px dashed #cfc7bb;display:flex;align-items:center;justify-content:center;font-size:7.5px;font-weight:700;letter-spacing:.06em;color:var(--gold)}

/* contact */
.contact{background:var(--dark);height:476px;position:relative;color:#fff}
.contact-title{position:absolute;left:276px;top:100px;font-family:var(--serif);font-weight:400;font-size:36px;line-height:1.2}
.contact-title em{display:block;color:var(--gold)}
.contact-lead{position:absolute;left:276px;top:226px;width:310px;font-size:12px;line-height:1.55;color:#c8c8c8;font-weight:300}
.contact-lines{position:absolute;left:276px;top:306px;list-style:none}
.contact-lines li{font-size:11px;margin-bottom:19px}
.contact-lines b{color:var(--gold);font-weight:700;display:inline-block;width:19px}
.inquiry{position:absolute;left:643px;top:100px;width:308px}
.field{border-bottom:1px solid #2e2e2e;height:82px}
.field label{display:block;font-size:7px;font-weight:700;color:var(--gold)}
.field .value{margin-top:14px;font-size:10px;color:#3a3a3a}
.field .value.set{color:#bcbcbc;display:flex;justify-content:space-between;padding:0 4px}
.submit{margin-top:25px;height:42px;background:var(--gold-fill);color:#1a1a1a;font-size:8px;font-weight:700;letter-spacing:.4em;display:flex;align-items:center;justify-content:center}

/* footer */
.site-footer{background:#0c0c0c;height:80px;display:flex;align-items:center;padding:0 27px 0 53px;font-size:7px;color:#505050}
.site-footer .brand-faint{letter-spacing:.4em;width:378px;font-size:8px}
.site-footer nav{display:flex;gap:31px;font-weight:600}
.site-footer .copy{margin-left:auto}
</style>
</head>
<body>

<header class="site-header">
  <div class="brand">VELMORA BRIGHTSTEAD</div>
  <nav class="main-nav">
    <a href="#">EXPERTISE</a><a href="#">INTELLIGENCE</a><a href="#">GLOBAL NETWORK</a><a href="#" class="connect">CONNECT</a>
  </nav>
</header>

<section class="hero">
  <h1 class="hero-title">Superior<em>Management</em>In High–Stakes<br>Law.</h1>
  <p class="hero-lead">Precision-engineered operational systems for elite firms. From custom implementation to proprietary judicial intelligence, we provide the infrastructure required for victory.</p>
  <div class="hero-photo" role="img" aria-label="Executive in a dark navy suit fastening his jacket">
    <div class="hero-badge">
      <div class="eyebrow">Established 2012</div>
      <p>Managing $4B+ in litigation assets across three continents.</p>
    </div>
  </div>
</section>

<section class="pillars">
  <div class="eyebrow">Service Protocol</div>
  <h2 class="section-title">The Operational Pillars</h2>
  <div class="pillar-count">01 — 04</div>
  <div class="pillar-grid">
    <article class="pillar">
      <svg viewBox="0 0 24 24"><path d="M12 3 3 7.5 12 12l9-4.5z"/><path d="m3 12 9 4.5 9-4.5"/><path d="m3 16.5 9 4.5 9-4.5"/></svg>
      <h3>Systems &amp;<br>Training</h3>
      <p>Full-spectrum tech implementation. Custom stack design, firm-wide onboarding, and security protocol audit.</p>
    </article>
    <article class="pillar">
      <svg viewBox="0 0 24 24"><circle cx="9" cy="8" r="4"/><path d="M2 21v-1a6 6 0 0 1 10-4.5"/><path d="m15 16 2 2 4-4"/></svg>
      <h3>Paralegal<br>Support</h3>
      <p>Specialized remote or in-office support. Caseload scaling, document drafting, and complex filing management.</p>
    </article>
    <article class="pillar">
      <svg viewBox="0 0 24 24"><path d="M21 3 3 10l7 3 3 7z"/><path d="m10 13 4-4"/></svg>
      <h3>Ex–Parte<br>Notice</h3>
      <p>Precision service by mail. High-priority notice administration and certified compliance tracking for ex-parte motions.</p>
    </article>
    <article class="pillar">
      <svg viewBox="0 0 24 24"><circle cx="11" cy="11" r="7"/><path d="m21 21-5-5"/></svg>
      <h3>Probate<br>Forensics</h3>
      <p>Heir hunting and asset location. Genealogical forensics to resolve complex estate liquidation and hidden assets.</p>
    </article>
  </div>
</section>

<section class="analytics">
  <div class="eyebrow">Strategic Assets</div>
  <h2 class="analytics-title">Judicial<em>Analytics.</em></h2>
  <p class="analytics-lead">We don’t just find case law; we profile the decision-makers. Our intelligence reports provide an unparalleled look at behavioral patterns in the courtroom.</p>
  <ul class="insight-list">
    <li class="insight"><span class="num">01</span><div><h4>Judge Motion History</h4><p>Comprehensive data on specific judge ruling patterns for summary judgments and discovery motions.</p></div></li>
    <li class="insight"><span class="num">02</span><div><h4>Opposing Counsel Research</h4><p>Historical filing analysis to identify tactical patterns, pressure points, and negotiation behaviors.</p></div></li>
  </ul>
  <div class="report-shadow"></div>
  <div class="report">
    <div class="report-head"><span>VELMORA INTELLIGENCE REPORT #882</span><span class="tag">CLASSIFIED</span></div>
    <div class="placeholder"></div>
    <div class="placeholder short"></div>
    <div class="metric">
      <div class="metric-row"><span>RULING SUCCESS RATE</span><b>84%</b></div>
      <div class="track"><i style="width:84%;background:var(--gold)"></i></div>
    </div>
    <div class="metric">
      <div class="metric-row"><span>OPPOSITION PATTERN</span><b>Predictable</b></div>
      <div class="track"><i style="width:92%;background:var(--ink)"></i></div>
    </div>
    <span class="report-btn">REQUEST SAMPLE INTEL</span>
  </div>
</section>

<section class="network">
  <h2 class="network-title">Cross-Border<br>Infrastructure.</h2>
  <p class="network-lead">Litigation is global. Our presence ensures your firm can operate with confidence across major financial and judicial hubs worldwide.</p>
  <ul class="network-facts">
    <li><svg viewBox="0 0 12 12"><circle cx="6" cy="6" r="5"/><path d="M1 6h10M6 1c2 2 2 8 0 10M6 1c-2 2-2 8 0 10"/></svg>3 GLOBAL REGIONAL HUBS</li>
    <li><svg viewBox="0 0 12 12"><path d="M7 1 2 7h4l-1 4 5-6H6z"/></svg>24/7 SUPPORT READINESS</li>
  </ul>
  <div class="hub-grid">
    <div class="hub"><h5>NYC</h5><span>HEADQUARTERS</span></div>
    <div class="hub"><h5>LDN</h5><span>EUROPEAN HUB</span></div>
    <div class="hub"><h5>SGP</h5><span>APAC OPERATIONS</span></div>
    <div class="hub"><h5>ZRH</h5><span>ASSET FORENSIC TEAM</span></div>
    <div class="hub"><h5>DXB</h5><span>LOGISTICS NODE</span></div>
    <div class="hub pending">EXPANDING 2026</div>
  </div>
</section>

<section class="contact">
  <h2 class="contact-title">Begin the<em>Evaluation.</em></h2>
  <p class="contact-lead">Confidential practice audits available for partners and managing directors. Optimize your firm’s structural performance today.</p>
  <ul class="contact-lines">
    <li><b>P</b>+1 212 555 0148</li>
    <li><b>E</b>intelligence@velmora-legal.example</li>
  </ul>
  <form class="inquiry">
    <div class="field"><label>FULL IDENTITY</label><div class="value">e.g. Marcus Ellery, Esq.</div></div>
    <div class="field" style="margin-top:0;height:82px;padding-top:0"><label style="margin-top:0">CORPORATE ENTITY</label><div class="value">Firm Name</div></div>
    <div class="field"><label>INTEREST NODE</label><div class="value set"><span>Systems Integration</span><span>⌄</span></div></div>
    <div class="submit">TRANSMIT INQUIRY</div>
  </form>
</section>

<footer class="site-footer">
  <div class="brand-faint">VELMORA BRIGHTSTEAD</div>
  <nav><span>METHODOLOGY</span><span>TRANSPARENCY</span><span>PRIVACY</span></nav>
  <div class="copy">© 2025 VELMORA MANAGEMENT. A GLOBAL INTELLIGENCE FIRM.</div>
</footer>

</body>
</html>
```